Design clean technology service-based company website

Hello, We are looking to reskin our company website. We are an environmental inspection company and test for Asbestos, Lead and Mold along with other contaminants. People depend on the results to be accurate and fast. We are regulated by the NQB and State regulations. We work a lot with business to business and business to customer. We are wanting to make our new presentation to be modern and easy for customers to interact with us, understand our process and services while providing valuable environmental informational resource and updates. We are a technology based company and will be providing instantaneous results as reports come in for the customers. We are needing good calls to action on the site to direct them to setup a new inspection. Each user will have a backend access to their job information with invoices, reports, status, etc. We have developed software to be able to proved these reports and want to look the part.

My current website is www.trylumaverde.com
Updates

Helllo we are wanting to make sure we have good time to select the right website for us and also have the additional time to select other pages of the website. We have received great designs and have consolidated our requests into a document for the next set of iterations.

Target Market(s)

Home Owners, Contractors, Engineers, Real Estate Agents, Building Owners, Insurance Adjusters

Industry/Entity Type

Environmental Consultant

Number of Pages Required

5+ page

Font styles to use
Sans Serif

Colors
0355a3
9bcb3c
7f7f7f
f5f5f5
000000

Requirements
Must have
• Use our existing logo to design around
• The layouts look good in mobile mode for understanding and selecting services and signing up
• Clean Modern Layout
• Have all pages on the website have a similar layout and feel
• Clearly communicate services along with bundle service packages
• Detail the customer journey with graphic design
• Great call to actions to either schedule inspection online, call, text, chat
Nice to have
• Have an interactive graphic for where to test for lead, asbestos and mold.
• I like the becky barlows top order line bar - see attached
• Have clear question and answer page layouts for asbestos, lead and mold
• Show Company reviews
• Have clear Resources pages for all types of contaminants
Should not have
• My current website is www.trylumaverde.com

```html
<!DOCTYPE html>
<html lang="en">
<head>
<meta charset="utf-8">
<title>LumaVerde — Environmental Testing</title>
<link href="https://fonts.googleapis.com/css2?family=Lato:wght@400;700;900&family=Montserrat:wght@400;600;700&display=swap" rel="stylesheet">
<style>
:root{
  --green:#8dc63f;
  --green-dark:#7bb32e;
  --ink:#1d1d1d;
  --dark:#262626;
  --darker:#1a1a1a;
  --grey:#7f7f7f;
  --light:#f5f5f5;
  --line:#e3e3e3;
  --white:#ffffff;
  --blue:#0355a3;
}
*{box-sizing:border-box;margin:0;padding:0}
html,body{width:1200px;height:5183px;overflow:hidden}
body{font-family:"Lato",sans-serif;color:var(--ink);background:var(--white);font-size:13px;line-height:1.6}
h1,h2,h3,h4{font-family:"Montserrat",sans-serif;font-weight:700}
.section-title{text-align:center;font-size:30px;color:var(--ink);margin-bottom:10px}
.section-sub{text-align:center;color:var(--grey);font-size:13px}
.btn-dark{display:inline-block;background:var(--darker);color:var(--white);font-family:"Montserrat",sans-serif;font-weight:700;font-size:12px;padding:14px 22px;letter-spacing:.5px}

/* header */
.site-header{height:120px;padding:0 45px;position:relative}
.site-header .brand{position:absolute;left:45px;top:42px}
.brand{display:flex;align-items:center;gap:10px}
.brand-dot{width:18px;height:18px;border-radius:50%;background:var(--green)}
.brand-name{font-family:"Lato",sans-serif;font-weight:900;font-size:30px;color:var(--green)}
.top-actions{position:absolute;right:45px;top:14px;display:flex;gap:8px}
.top-actions span{background:var(--darker);color:var(--white);font-size:10px;padding:6px 12px}
.top-actions span.green{background:var(--green)}
.main-nav{position:absolute;right:45px;top:72px;display:flex;gap:34px;font-family:"Montserrat",sans-serif;font-size:11px;font-weight:600;color:#444}
.main-nav .active{color:var(--green)}

/* hero */
.hero{height:590px;position:relative;background:linear-gradient(180deg,#d9e6ee 0%,#b8c9d4 35%,#5e5e5e 60%,#3a3a3a 100%)}
.hexes{position:absolute;top:120px;left:0;width:100%}
.hex{position:absolute;width:236px;height:260px;text-align:center;color:var(--white)}
.hex svg{position:absolute;inset:0}
.hex-body{position:relative;padding:38px 34px 0}
.hex-symbol{font-family:"Montserrat",sans-serif;font-size:58px;font-weight:700;line-height:1}
.hex-label{display:inline-block;background:var(--darker);font-size:11px;font-weight:700;padding:4px 12px;margin:10px 0 8px}
.hex-text{font-size:10px;line-height:1.45}

/* welcome */
.welcome{height:215px;padding:40px 170px 0;text-align:center}
.welcome h2{font-size:22px;margin-bottom:14px}
.welcome p{color:var(--grey);font-size:11.5px;margin-bottom:10px}

/* next step */
.next-step{height:430px;display:flex}
.owner{width:660px;padding:50px 40px 0 40px;position:relative}
.owner-photo{position:absolute;left:40px;top:50px;width:140px;height:170px;background:linear-gradient(180deg,#c9ced3,#8d949a)}
.owner-caption{position:absolute;left:40px;top:228px;font-weight:700;font-size:13px}
.owner-text{margin-left:160px;color:#444;font-size:13px;line-height:1.7}
.signature-area{margin:24px 0 0 160px;width:150px;height:50px;background:linear-gradient(90deg,#eee,#f8f8f8)}
.next-panel{flex:1;background:var(--green);color:var(--white);padding:60px 50px 0 50px}
.next-panel h3{font-size:24px;margin-bottom:14px}
.next-panel p{font-size:12px;line-height:1.7;margin-bottom:26px}

/* services */
.services{height:445px;padding-top:60px}
.service-row{display:flex;justify-content:center;gap:30px;margin-top:55px;padding:0 100px}
.service{width:180px;text-align:center}
.service-icon{width:78px;height:78px;margin:0 auto 16px;border:2px solid var(--green);border-radius:50%;display:flex;align-items:center;justify-content:center}
.service h4{font-size:11px;margin-bottom:8px}
.service p{color:var(--grey);font-size:10.5px;line-height:1.5}

/* why choose */
.why{height:545px;display:flex}
.why-media{width:680px;background:linear-gradient(135deg,#cfd3d6 0%,#9aa0a5 45%,#4d5154 100%)}
.why-copy{flex:1;background:var(--light);padding:55px 45px 0}
.why-copy h2{font-size:30px;margin-bottom:22px}
.why-copy h4{font-size:11px;color:var(--green);margin-bottom:6px}
.why-copy p{color:var(--grey);font-size:11px;margin-bottom:22px}

/* cta band */
.cta-band{height:190px;background:var(--green);color:var(--white);padding:42px 60px 0;position:relative}
.cta-band .kicker{font-family:"Montserrat",sans-serif;font-weight:700;font-size:14px}
.cta-band h3{font-size:22px;margin:4px 0 14px}
.cta-opts{display:flex;gap:26px;font-size:12px;font-weight:700}
.cta-opts span{display:flex;align-items:center;gap:7px}
.cta-opts i{width:14px;height:14px;background:var(--white);display:inline-block}
.cta-band .btn-dark{position:absolute;right:60px;top:80px}

/* qa */
.qa{height:685px;padding-top:40px}
.qa-tabs{display:flex;margin:30px 60px 0;border-bottom:1px solid var(--line)}
.qa-tabs span{padding:10px 22px;font-size:11px;color:#555}
.qa-tabs .on{border:1px solid var(--line);border-bottom-color:var(--white);margin-bottom:-1px;color:var(--green);font-weight:700}
.qa-body{display:flex;gap:30px;margin:24px 60px 0}
.qa-list{width:470px}
.qa-item{border:1px solid var(--line);padding:12px 16px;font-size:11.5px;font-weight:700;margin-bottom:8px}
.qa-item p{font-weight:400;color:var(--grey);font-size:11px;margin-top:10px;line-height:1.7}
.qa-art{flex:1;height:440px;background:linear-gradient(180deg,#f3f3f3,#dcdcdc)}

/* testimonials */
.testimonials{height:300px;background:var(--green-dark);color:var(--white);text-align:center;padding-top:32px}
.testimonials h2{font-size:16px;letter-spacing:1px}
.client-avatar{width:64px;height:64px;border-radius:50%;background:#d8dcd0;border:3px solid var(--white);margin:22px auto 14px}
.testimonials blockquote{font-size:13px;max-width:640px;margin:0 auto 10px}
.testimonials .who{font-weight:700;font-size:12px}

/* blog */
.blog{height:570px;padding-top:45px}
.blog-row{display:flex;gap:40px;padding:0 175px;margin-top:36px}
.post{width:260px}
.post-img{height:170px;margin-bottom:14px}
.post h4{font-size:13px;margin-bottom:8px}
.post p{color:var(--grey);font-size:11px}

/* signup */
.signup{height:310px;background:linear-gradient(180deg,#2d2d2d,#1e1e1e);color:var(--white);display:flex;padding:55px 60px 0}
.signup-copy{width:600px}
.signup-copy h2{font-family:"Lato",sans-serif;font-weight:400;font-size:30px;line-height:1.3;margin-bottom:14px}
.signup-copy h2 b{color:var(--green);font-weight:400}
.signup-copy p{color:#bbb;font-size:11.5px;max-width:440px}
.signup-form{flex:1}
.field{height:34px;border:1px solid #555;margin-bottom:8px;padding:8px 12px;color:#aaa;font-size:11px;background:#2a2a2a}
.field.tall{height:70px}
.submit{background:var(--green);color:var(--white);font-weight:700;font-size:11px;padding:9px 30px;display:inline-block}

/* accreditations */
.accreditations{height:330px;padding-top:55px}
.badges{display:flex;justify-content:center;align-items:center;gap:80px;margin-top:60px}
.badge{background:#cfcfcf}

/* footer */
.site-footer{height:378px;background:var(--darker);color:#bbb;position:relative}
.contact-strip{display:flex;gap:110px;padding:22px 0 0 210px;font-size:10.5px}
.contact-strip div{display:flex;gap:10px;align-items:flex-start}
.contact-strip b{color:var(--white);display:block}
.footer-cols{display:flex;gap:40px;padding:36px 60px 0}
.footer-brand{width:280px}
.footer-brand p{font-size:10.5px;margin:12px 0 12px}
.footer-badge{width:110px;height:34px;background:#4a4a4a}
.footer-col{width:170px;font-size:10.5px}
.footer-col h5{color:var(--white);font-family:"Montserrat",sans-serif;font-size:12px;margin-bottom:12px}
.footer-col li{list-style:none;margin-bottom:6px}
.news-box{display:flex;margin-top:10px}
.news-box span{flex:1;height:30px;background:#333}
.news-box i{width:32px;height:30px;background:var(--green)}
.bottom-bar{position:absolute;left:0;right:0;bottom:0;height:40px;background:#111;display:flex;align-items:center;justify-content:space-between;padding:0 60px;font-size:10px}
.socials{display:flex;gap:8px}
.socials i{width:18px;height:18px;border-radius:50%;background:#444;display:block}
</style>
</head>
<body>

<header class="site-header">
  <div class="brand"><span class="brand-dot"></span><span class="brand-name">LumaVerde</span></div>
  <div class="top-actions"><span>(555) 014-2290</span><span class="green">Book A New Inspection</span><span>Login</span></div>
  <nav class="main-nav"><span class="active">HOME</span><span>OUR SERVICES</span><span>RESOURCES</span><span>BLOG</span><span>FAQS</span><span>REVIEWS</span><span>CONTACT</span><span>⌕</span></nav>
</header>

<section class="hero" role="img" aria-label="Inspector in protective gear working on a house roof under a bright sky">
  <div class="hexes">
    <div class="hex" style="left:153px">
      <svg viewBox="0 0 236 260" width="236" height="260"><polygon points="118,0 236,65 236,195 118,260 0,195 0,65" fill="#8dc63f"/></svg>
      <div class="hex-body"><div class="hex-symbol">As</div><div class="hex-label">Asbestos Inspections</div><div class="hex-text">Fast, fully certified asbestos testing for homes and buildings with results you can trust.</div></div>
    </div>
    <div class="hex" style="left:452px">
      <svg viewBox="0 0 236 260" width="236" height="260"><polygon points="118,0 236,65 236,195 118,260 0,195 0,65" fill="#8dc63f"/></svg>
      <div class="hex-body"><div class="hex-symbol">Mo</div><div class="hex-label">Mold Inspections</div><div class="hex-text">Air and surface mold sampling that finds the source and keeps your family safe.</div></div>
    </div>
    <div class="hex" style="left:767px">
      <svg viewBox="0 0 236 260" width="236" height="260"><polygon points="118,0 236,65 236,195 118,260 0,195 0,65" fill="#8dc63f"/></svg>
      <div class="hex-body"><div class="hex-symbol">Pb</div><div class="hex-label">Lead Inspections</div><div class="hex-text">Lead paint and dust testing for older homes, rentals and renovation projects.</div></div>
    </div>
  </div>
</section>

<section class="welcome">
  <h2>Welcome to Environmental Testing Evolved</h2>
  <p>Everyone wants peace of mind about the air they breathe and the spaces they share. Our certified team tests for asbestos, mold and lead with modern lab methods and clear reports delivered straight to your online account so you can act with confidence.</p>
  <p>From homeowners and contractors to engineers and property managers, we make the inspection process simple. Book online, track your job status in real time and download results the moment they arrive from the lab.</p>
</section>

<section class="next-step">
  <div class="owner">
    <div class="owner-photo" role="img" aria-label="Portrait of the company owner"></div>
    <div class="owner-caption">Owner</div>
    <p class="owner-text">In my experience with inspecting property and mitigating environmental issues, I know how stressful a test result can be. We built this company so every client gets fast answers, honest advice and reports that are easy to understand.</p>
    <div class="signature-area" role="img" aria-label="Owner's handwritten signature"></div>
  </div>
  <div class="next-panel">
    <h3>The Next Step</h3>
    <p>Scheduling your inspection is quick. Choose a service, pick a time that suits you and our certified inspector will arrive ready to sample. Results are posted to your secure portal as soon as the lab reports in, with guidance on what to do next.</p>
    <span class="btn-dark">CALL NOW: (555) 014-2290</span>
  </div>
</section>

<section class="services">
  <h2 class="section-title">Our Services</h2>
  <p class="section-sub">Accurate results from certified inspectors using trusted laboratory methods</p>
  <div class="service-row">
    <div class="service"><div class="service-icon"><svg width="34" height="34" viewBox="0 0 34 34" fill="none" stroke="#8dc63f" stroke-width="2"><path d="M5 17 17 6l12 11v12H5z"/></svg></div><h4>ASBESTOS INSPECTION</h4><p>Bulk and air sampling for homes and commercial buildings.</p></div>
    <div class="service"><div class="service-icon"><svg width="34" height="34" viewBox="0 0 34 34" fill="none" stroke="#8dc63f" stroke-width="2"><circle cx="17" cy="17" r="10"/><circle cx="17" cy="17" r="3"/></svg></div><h4>MOLD INSPECTION</h4><p>Moisture mapping and spore testing to locate growth.</p></div>
    <div class="service"><div class="service-icon"><svg width="34" height="34" viewBox="0 0 34 34" fill="none" stroke="#8dc63f" stroke-width="2"><rect x="8" y="8" width="18" height="18"/><path d="M8 17h18"/></svg></div><h4>LEAD INSPECTION</h4><p>Paint, dust and soil testing for older properties.</p></div>
    <div class="service"><div class="service-icon"><svg width="34" height="34" viewBox="0 0 34 34" fill="none" stroke="#8dc63f" stroke-width="2"><path d="M17 5v24M9 13l8-8 8 8"/></svg></div><h4>RADON</h4><p>Short and long term radon tests with clear guidance.</p></div>
    <div class="service"><div class="service-icon"><svg width="34" height="34" viewBox="0 0 34 34" fill="none" stroke="#8dc63f" stroke-width="2"><path d="M8 18l6 6 12-14"/></svg></div><h4>OTHER SERVICES</h4><p>Indoor air quality and custom contaminant testing.</p></div>
  </div>
</section>

<section class="why">
  <div class="why-media" role="img" aria-label="Video still of a technician in a white protective suit spraying during abatement"></div>
  <div class="why-copy">
    <h2>Why Choose Us</h2>
    <h4>WE'RE SERIOUS ABOUT OUR WORK</h4>
    <p>Our inspectors are fully certified and follow every state and federal protocol on every job, large or small.</p>
    <h4>FAST, ACCURATE TEST RESULTS, VERY FAST</h4>
    <p>Our labs report quickly and results appear in your portal instantly, so projects keep moving without costly delays.</p>
    <h4>WE TREAT YOUR FAMILY AND BUSINESS LIKE OURS</h4>
    <p>We explain every finding in plain language and help you plan the right next step for your property.</p>
  </div>
</section>

<section class="cta-band">
  <div class="kicker">We Offer 24/7 Same Day Services</div>
  <h3>Call LumaVerde Now for Fast, Reliable Asbestos Home Inspections</h3>
  <div class="cta-opts"><span><i></i>Commercial</span><span><i></i>Residential</span><span><i></i>Home Owner and Contractor Service</span></div>
  <span class="btn-dark">CALL NOW: (555) 014-2290</span>
</section>

<section class="qa">
  <h2 class="section-title">Q &amp; A</h2>
  <p class="section-sub">Quick answers to the questions we hear most often from our customers</p>
  <div class="qa-tabs"><span class="on">Asbestos Inspection</span><span>Mold Inspection</span><span>Lead Inspection</span><span>FAQ</span><span>Resources</span></div>
  <div class="qa-body">
    <div class="qa-list">
      <div class="qa-item">What do I do if my home contains asbestos materials and I am planning a remodel or repair?
        <p>Do not disturb the material. Schedule an inspection so our certified team can sample suspect areas and confirm what is present. Once results arrive we will explain your options, from leaving stable material in place to hiring a licensed abatement contractor before work begins. Many state rules require testing before any renovation, and our reports meet those requirements for permits and contractors.</p>
      </div>
      <div class="qa-item">I have signs of water damage and think I have mold. How soon should I test?</div>
      <div class="qa-item">Which homes are most likely to contain lead paint?</div>
      <div class="qa-item">Are your results accepted by local building officials?</div>
    </div>
    <div class="qa-art" role="img" aria-label="Cutaway drawing of a two-storey house showing where contaminants are found"></div>
  </div>
</section>

<section class="testimonials">
  <h2>WHAT OUR CLIENTS SAY</h2>
  <div class="client-avatar" role="img" aria-label="Client portrait"></div>
  <blockquote>"The inspector arrived on time, explained each step and our results were in the portal two days later. I would recommend this team to anyone buying an older home."</blockquote>
  <div class="who">— Marcus Ellery</div>
</section>

<section class="blog">
  <h2 class="section-title">Our Blog</h2>
  <p class="section-sub">Practical guides and updates on asbestos, mold, lead and healthy indoor air</p>
  <div class="blog-row">
    <article class="post"><div class="post-img" role="img" aria-label="Family smiling on a sofa at home" style="background:linear-gradient(135deg,#e9d9c4,#b59a7a)"></div><h4>4 Reasons to Get a Home Inspection for Asbestos</h4><p>Older homes often hide asbestos in flooring, ceilings and pipe wrap. Here is why testing first matters.</p></article>
    <article class="post"><div class="post-img" role="img" aria-label="Close view of mold growth on a wall" style="background:linear-gradient(135deg,#dcdcd2,#6f7566)"></div><h4>Mold Testing and Three Preventable Problems</h4><p>Simple habits that stop moisture and mold before they become a costly repair job.</p></article>
    <article class="post"><div class="post-img" role="img" aria-label="Contractor and homeowner reviewing a report" style="background:linear-gradient(135deg,#d7dde2,#8a97a3)"></div><h4>Why Use LumaVerde for Asbestos Testing</h4><p>Certified sampling and quick lab turnaround keep your renovation project on schedule.</p></article>
  </div>
</section>

<section class="signup">
  <div class="signup-copy">
    <h2>Have any questions? <b>Sign Up</b><br>for a new <b>Inspection.</b></h2>
    <p>Send us a short message and a member of our team will reply within one business day to answer questions or book your inspection time.</p>
  </div>
  <div class="signup-form">
    <div class="field">Name</div>
    <div class="field">Email</div>
    <div class="field tall">Message</div>
    <span class="submit">SUBMIT</span>
  </div>
</section>

<section class="accreditations">
  <h2 class="section-title">Our Accreditations</h2>
  <div class="badges">
    <div class="badge" style="width:150px;height:60px" role="img" aria-label="NQB accreditation badge"></div>
    <div class="badge" style="width:150px;height:60px" role="img" aria-label="Industry certification badge"></div>
    <div class="badge" style="width:170px;height:60px" role="img" aria-label="State public health department badge"></div>
    <div class="badge" style="width:70px;height:70px;border-radius:50%" role="img" aria-label="Certification seal"></div>
  </div>
</section>

<footer class="site-footer">
  <div class="contact-strip">
    <div><svg width="16" height="18" viewBox="0 0 16 18"><path d="M8 1a6 6 0 0 1 6 6c0 5-6 10-6 10S2 12 2 7a6 6 0 0 1 6-6z" fill="#8dc63f"/></svg><span><b>ADDRESS</b>88 Fernridge Ave, Suite 4, Alder Falls</span></div>
    <div><svg width="16" height="16" viewBox="0 0 16 16"><path d="M3 1h3l1 4-2 1a9 9 0 0 0 5 5l1-2 4 1v3a2 2 0 0 1-2 2A13 13 0 0 1 1 3a2 2 0 0 1 2-2z" fill="#8dc63f"/></svg><span><b>PHONE</b>(555) 014-2290</span></div>
    <div><svg width="18" height="14" viewBox="0 0 18 14"><rect x="1" y="1" width="16" height="12" fill="none" stroke="#8dc63f" stroke-width="2"/><path d="M1 1l8 7 8-7" fill="none" stroke="#8dc63f" stroke-width="2"/></svg><span><b>EMAIL</b>hello@trylumaverde.com</span></div>
  </div>
  <div class="footer-cols">
    <div class="footer-brand">
      <div class="brand"><span class="brand-dot"></span><span class="brand-name" style="font-size:26px">LumaVerde</span></div>
      <p>We are committed to accurate, fast environmental testing for homes and businesses across the region.</p>
      <div class="footer-badge" role="img" aria-label="Business accreditation badge"></div>
    </div>
    <div class="footer-col"><h5>LINKS</h5><ul><li>Home</li><li>Our Services</li><li>Resources</li><li>Blog</li><li>Contact</li></ul></div>
    <div class="footer-col" style="width:250px"><h5>FAQ</h5><ul><li>How do I book an inspection?</li><li>How fast are lab results?</li><li>Do you test rental homes?</li><li>Can I view my invoices online?</li></ul></div>
    <div class="footer-col" style="width:260px"><h5>NEWSLETTER</h5><p>Get testing tips and regulation updates in your inbox.</p><div class="news-box"><span></span><i></i></div></div>
  </div>
  <div class="bottom-bar"><span>© Copyright LumaVerde. All rights reserved.</span><div class="socials"><i></i><i></i><i></i><i></i></div></div>
</footer>

</body>
</html>
```